Estate Agent/Real Estate valuation tool

We need a design for our our new estate agent valuation tool.

The tool allows users to book a valuation of their house/property with the estate agent, after they choose there property they can then complete their details and choose a booking time.

The mock up of the design we want is attached to this project.(Main Screen)

This also needs to be responsive so the design is easy to use on a mobile device.

Target Market(s)

estate agents

Industry/Entity Type

Real Estate Agent

Number of Pages Required

1 page

Requirements
Must have
• Section 2 and 3 greyed out when user is on step 1
• Section 1 and 3 greyed out when user is on step 2
• Section 1 and 2 greyed out when the user is on step 3
• *** Design must be shown for mobile/ipad and desktop
Nice to have
• Clean and Simple
Should not have
• Dark colours

```html
<!DOCTYPE html>
<html lang="en">
<head>
<meta charset="utf-8">
<title>Book your Valuation Online</title>
<link rel="stylesheet" href="https://fonts.googleapis.com/css2?family=Cinzel:wght@400;700&family=Lato:wght@400;700&display=swap">
<style>
  :root {
    --page-bg: #e4e4e4;
    --sky-top: #7fa3cf;
    --sky-mid: #c9d3de;
    --haze: #dcdcdc;
    --brand-blue: #2f74c0;
    --brand-blue-deep: #1e4e78;
    --input-blue: #3b7bc0;
    --ink: #111111;
    --field-grey: rgba(150, 150, 150, 0.55);
    --field-text: #1b1b1b;
    --card-bg: rgba(228, 228, 228, 0.78);
    --card-rule: #9a9a9a;
    --search-bg: #222222;
    --white: #ffffff;
  }
  * { box-sizing: border-box; margin: 0; padding: 0; }
  html, body {
    width: 1200px; height: 852px; overflow: hidden;
    background: var(--page-bg);
    font-family: "Lato", "Helvetica Neue", Arial, sans-serif;
  }
  .screen {
    position: absolute; left: 320px; top: 6px;
    width: 560px; height: 840px; overflow: hidden;
  }
  .hero-photo {
    position: absolute; inset: 0;
    background:
      radial-gradient(ellipse at 30% 55%, rgba(120,120,120,0.45), transparent 60%),
      linear-gradient(180deg, var(--sky-top) 0%, var(--sky-mid) 22%, var(--haze) 55%, #c4c4c4 100%);
  }
  .brand-mark {
    position: absolute; left: 190px; top: 19px; width: 187px; height: 77px;
    background: var(--brand-blue); border-radius: 8px;
    display: flex; align-items: center; justify-content: center;
    font-family: "Cinzel", Georgia, serif; font-size: 36px; color: var(--white);
  }
  .page-title {
    position: absolute; left: 0; right: 0; top: 110px;
    text-align: center; font-family: "Cinzel", Georgia, serif;
    font-weight: 700; font-size: 34px; line-height: 33px; color: var(--ink);
  }
  .step-badge {
    position: absolute; left: 190px; top: 206px; width: 180px; height: 38px;
    background: var(--brand-blue); border-radius: 6px 6px 0 0;
    color: var(--white); font-size: 20px; letter-spacing: 1px;
    display: flex; align-items: center; justify-content: center;
  }
  .details-card {
    position: absolute; left: 22px; top: 247px; width: 518px; height: 588px;
    background: var(--card-bg); border-radius: 14px; overflow: hidden;
    box-shadow: 0 2px 10px rgba(0,0,0,0.18);
  }
  .card-heading {
    height: 75px; border-bottom: 2px solid var(--card-rule);
    display: flex; align-items: center; justify-content: center;
    font-family: "Cinzel", Georgia, serif; font-size: 32px; letter-spacing: 1px; color: var(--ink);
  }
  .field-label {
    position: absolute; left: 45px; top: 112px;
    font-size: 23px; letter-spacing: 1px; color: var(--ink);
  }
  .postcode-input {
    position: absolute; left: 40px; top: 154px; width: 317px; height: 53px;
    background: var(--input-blue); border-radius: 4px;
  }
  .search-button {
    position: absolute; left: 364px; top: 154px; width: 115px; height: 53px;
    background: var(--search-bg); border-radius: 4px; color: var(--white);
    font-weight: 700; font-size: 21px; letter-spacing: 1px;
    display: flex; align-items: center; justify-content: center;
  }
  .address-field {
    position: absolute; left: 40px; width: 439px; height: 53px;
    background: var(--field-grey); border-radius: 4px;
    padding-left: 18px; display: flex; align-items: center;
    font-size: 24px; letter-spacing: 1.5px; color: var(--field-text);
  }
  .address-street { top: 233px; }
  .address-city { top: 312px; }
  .address-county { top: 391px; }
  .proceed-button {
    position: absolute; left: 0; bottom: 0; width: 100%; height: 91px;
    background: linear-gradient(90deg, var(--brand-blue) 0%, #2a6aa8 55%, var(--brand-blue-deep) 100%);
    border-top: 2px solid #8a8a8a;
    color: var(--white); font-size: 26px; letter-spacing: 2px;
    display: flex; align-items: center; justify-content: center;
  }
</style>
</head>
<body>
  <main class="screen">
    <div class="hero-photo" role="img" aria-label="Softly blurred photograph of a house against a blue sky"></div>
    <div class="brand-mark">LOGO</div>
    <h1 class="page-title">Book your<br>Valuation Online</h1>
    <div class="step-badge">STEP 1 of 3</div>
    <section class="details-card">
      <h2 class="card-heading">PROPERTY DETAILS</h2>
      <div class="field-label">POSTAL CODE</div>
      <div class="postcode-input"></div>
      <div class="search-button">SEARCH</div>
      <div class="address-field address-street">123 Test Street</div>
      <div class="address-field address-city">Test City</div>
      <div class="address-field address-county">Test County</div>
      <div class="proceed-button">PROCEED</div>
    </section>
  </main>
</body>
</html>
```